The name of the company is Torvend Holdings, LLC. I would like a business card with a logo.

On the top left, I would like a logo design of a crown and I would like Torvend over the top of the crown while Holdings on the bottom. Please see attached files as an example of crown and positioning of Torvend Holdings. Then I would like the letters TH in the middle(see picture).

Colors

Designer to choose colors to be used in the design.

```html
<!DOCTYPE html>
<html lang="en">
<head>
<meta charset="UTF-8">
<title>Torvend Holdings, LLC — Business Card</title>
<link href="https://fonts.googleapis.com/css2?family=Montserrat:wght@400;600;700&display=swap" rel="stylesheet">
<style>
  :root {
    --backdrop: #e9ebee;
    --card: #ffffff;
    --brand-blue: #0b4ea2;
    --ink: #3b3b3b;
    --ring: #1e5cb3;
  }
  * { box-sizing: border-box; margin: 0; padding: 0; }
  html, body {
    width: 1200px; height: 900px; overflow: hidden;
    background: var(--backdrop);
    font-family: "Montserrat", sans-serif;
  }
  .business-card {
    position: absolute;
    left: 100px; top: 165px;
    width: 1000px; height: 570px;
    background: var(--card);
    box-shadow: 0 10px 30px rgba(0,0,0,0.18);
  }
  .brand-mark {
    position: absolute;
    left: 70px; top: 45px;
    width: 210px; height: 210px;
    border: 2px solid var(--ring);
    border-radius: 50%;
    display: flex; align-items: center; justify-content: center;
    text-align: center;
  }
  .brand-mark__name {
    color: var(--brand-blue);
    font-weight: 700;
    font-size: 22px;
    letter-spacing: 1px;
    line-height: 1.3;
    text-transform: uppercase;
  }
  .holder {
    position: absolute;
    right: 60px; top: 135px;
    text-align: right;
  }
  .holder__name {
    color: var(--brand-blue);
    font-weight: 700;
    font-size: 30px;
    letter-spacing: 0.5px;
  }
  .holder__title {
    color: var(--ink);
    font-size: 22px;
    margin-top: 2px;
    letter-spacing: 0.5px;
  }
  .accent-bar {
    position: absolute;
    right: 0; top: 148px;
    width: 8px; height: 48px;
    background: var(--brand-blue);
  }
  .contact {
    position: absolute;
    left: 70px; top: 300px;
    color: var(--ink);
    font-size: 22px;
    line-height: 1.3;
    letter-spacing: 0.4px;
  }
  .contact__company {
    color: var(--brand-blue);
    font-weight: 700;
    font-size: 24px;
    letter-spacing: 1px;
    margin-bottom: 4px;
  }
  .contact__row {
    display: flex; align-items: center; gap: 10px;
  }
  .contact__icon { width: 22px; height: 22px; flex: none; }
</style>
</head>
<body>
  <main class="business-card">
    <div class="brand-mark">
      <span class="brand-mark__name">Torvend<br>Holdings</span>
    </div>

    <div class="holder">
      <p class="holder__name">Dara Kensington, MBA</p>
      <p class="holder__title">Founder | CEO</p>
    </div>
    <div class="accent-bar"></div>

    <section class="contact">
      <p class="contact__company">TORVEND HOLDINGS, LLC</p>
      <p>412 Harlow Crest Road, Suite 310</p>
      <p>Maple Ridge Park, CA. 90518</p>
      <p class="contact__row">
        <svg class="contact__icon" viewBox="0 0 24 24" aria-hidden="true">
          <circle cx="12" cy="12" r="12" fill="#0b4ea2"/>
          <path d="M8.5 6.5l2 .3.8 2.6-1.4 1.2a8 8 0 0 0 3.5 3.5l1.2-1.4 2.6.8.3 2c-.5.8-1.5 1.2-2.6 1-3.8-.8-6.9-3.9-7.7-7.7-.2-1.1.2-2.1 1.3-2.3z" fill="#fff"/>
        </svg>
        (555) 214-7089
      </p>
      <p class="contact__row">
        <svg class="contact__icon" viewBox="0 0 24 24" aria-hidden="true">
          <circle cx="12" cy="12" r="12" fill="#0b4ea2"/>
          <rect x="6" y="8" width="12" height="8.5" rx="1" fill="none" stroke="#fff" stroke-width="1.4"/>
          <path d="M6.3 8.5l5.7 4.3 5.7-4.3" fill="none" stroke="#fff" stroke-width="1.4"/>
        </svg>
        torvend.holdings@mailbox.com
      </p>
    </section>
  </main>
</body>
</html>
```